Brookhaven Dentistry- Larkspur Commons

Windows graphics, photos, advertising website and logo

Colors

Designer to choose colors to be used in the design.

```html
<!DOCTYPE html>
<html lang="en">
<head>
<meta charset="utf-8">
<title>Brookhaven Dentistry- Larkspur Commons — Window Graphics</title>
<link rel="stylesheet" href="https://fonts.googleapis.com/css2?family=Montserrat:wght@700&display=swap">
<style>
  :root {
    --backdrop: #38383a;
    --ink: #000000;
    --brand-red: #e3161f;
    --deep-red: #8a0a10;
    --paper: #ffffff;
    --frame: #4a4a4a;
  }
  html, body {
    margin: 0;
    padding: 0;
    width: 1200px;
    height: 960px;
    overflow: hidden;
    background: var(--backdrop);
    font-family: "Montserrat", Arial, sans-serif;
  }
  .window-set {
    position: relative;
    width: 1200px;
    height: 960px;
  }
  .pane {
    position: absolute;
    display: block;
    outline: 1px solid var(--frame);
  }
  .pane--tall { top: 288px; width: 198px; height: 290px; }
  .pane--door { top: 413px; left: 443px; width: 109px; height: 237px; }
  .kickplate {
    position: absolute;
    top: 582px;
    width: 198px;
    height: 90px;
    background: var(--ink);
    outline: 1px solid var(--frame);
  }
  .col-1 { left: 37px; }
  .col-2 { left: 240px; }
  .col-4 { left: 559px; }
  .col-5 { left: 762px; }
  .col-6 { left: 966px; }
  .brand-name, .web-address {
    font-family: "Montserrat", Arial, sans-serif;
    font-weight: 700;
  }
  .brand-name { fill: var(--brand-red); }
  .web-address { fill: var(--paper); }
</style>
</head>
<body>
<main class="window-set">

  <svg class="pane pane--tall col-1" viewBox="0 0 247 362" aria-label="Window graphic with family photo and web address">
    <defs>
      <linearGradient id="glow-1" x1="0" y1="0" x2="0" y2="1">
        <stop offset="0" stop-color="#000"/><stop offset="1" stop-color="#c8121a"/>
      </linearGradient>
      <linearGradient id="photo-1" x1="0" y1="0" x2="1" y2="1">
        <stop offset="0" stop-color="#f3f1ee"/><stop offset="0.5" stop-color="#b77a5a"/><stop offset="1" stop-color="#8c4f3b"/>
      </linearGradient>
    </defs>
    <rect width="247" height="362" fill="#000"/>
    <rect y="322" width="247" height="40" fill="url(#glow-1)"/>
    <path role="img" aria-label="Photo of a smiling mother with her son and daughter" d="M0 0H247V222C170 230 90 258 0 285Z" fill="url(#photo-1)"/>
    <path d="M0 288C90 262 170 232 247 222" stroke="var(--brand-red)" stroke-width="9" fill="none"/>
    <path d="M0 300C90 270 170 242 247 236" stroke="var(--brand-red)" stroke-width="3" fill="none"/>
    <text class="web-address" x="123.5" y="324" text-anchor="middle" font-size="12.5">mybrookhavendentistry.com</text>
  </svg>
  <div class="kickplate col-1"></div>

  <svg class="pane pane--tall col-2" viewBox="0 0 247 362" aria-label="Window graphic with brand name and couple photo">
    <defs>
      <linearGradient id="glow-2" x1="0" y1="0" x2="0" y2="1">
        <stop offset="0" stop-color="#c8121a"/><stop offset="1" stop-color="#000"/>
      </linearGradient>
      <linearGradient id="photo-2" x1="0" y1="0" x2="1" y2="1">
        <stop offset="0" stop-color="#d9b49a"/><stop offset="0.6" stop-color="#a8765a"/><stop offset="1" stop-color="#f0e6dc"/>
      </linearGradient>
    </defs>
    <rect width="247" height="362" fill="#000"/>
    <rect width="247" height="40" fill="url(#glow-2)"/>
    <text class="brand-name" x="123.5" y="62" text-anchor="middle" font-size="29">Brookhaven</text>
    <text class="brand-name" x="200" y="85" text-anchor="end" font-size="12" letter-spacing="4">DENTISTRY</text>
    <path role="img" aria-label="Photo of a smiling young couple" d="M0 155C90 150 150 108 247 112V362H0Z" fill="url(#photo-2)"/>
    <path d="M0 150C90 145 150 102 247 104" stroke="var(--brand-red)" stroke-width="9" fill="none"/>
    <path d="M0 138C90 132 150 96 247 92" stroke="var(--brand-red)" stroke-width="3" fill="none"/>
  </svg>
  <div class="kickplate col-2"></div>

  <svg class="pane pane--door" viewBox="0 0 136 296" aria-label="Door graphic with web address">
    <defs>
      <linearGradient id="glow-3" x1="0" y1="0" x2="0" y2="1">
        <stop offset="0" stop-color="#c8121a"/><stop offset="1" stop-color="#000"/>
      </linearGradient>
    </defs>
    <rect width="136" height="296" fill="#000"/>
    <rect width="136" height="40" fill="url(#glow-3)"/>
    <circle cx="68" cy="140" r="42" fill="none" stroke="var(--brand-red)" stroke-width="7"/>
    <path d="M0 196C40 204 80 236 136 244" stroke="var(--brand-red)" stroke-width="6" fill="none"/>
    <path d="M0 208C40 216 80 244 136 252" stroke="var(--brand-red)" stroke-width="2" fill="none"/>
    <text class="web-address" x="68" y="278" text-anchor="middle" font-size="7.5">mybrookhavendentistry.com</text>
  </svg>

  <svg class="pane pane--tall col-4" viewBox="0 0 247 362" aria-label="Window graphic with brand name and child photo">
    <defs>
      <linearGradient id="glow-4" x1="0" y1="0" x2="0" y2="1">
        <stop offset="0" stop-color="#c8121a"/><stop offset="1" stop-color="#000"/>
      </linearGradient>
      <linearGradient id="photo-4" x1="0" y1="0" x2="1" y2="1">
        <stop offset="0" stop-color="#d8b66a"/><stop offset="0.5" stop-color="#e7c98a"/><stop offset="1" stop-color="#e4d642"/>
      </linearGradient>
    </defs>
    <rect width="247" height="362" fill="#000"/>
    <rect width="247" height="40" fill="url(#glow-4)"/>
    <text class="brand-name" x="123.5" y="62" text-anchor="middle" font-size="29">Brookhaven</text>
    <text class="brand-name" x="220" y="85" text-anchor="end" font-size="12" letter-spacing="4">DENTISTRY</text>
    <path role="img" aria-label="Photo of a smiling boy with glasses in a play area" d="M0 102C80 100 140 150 247 155V362H0Z" fill="url(#photo-4)"/>
    <path d="M0 98C80 96 140 146 247 151" stroke="var(--brand-red)" stroke-width="9" fill="none"/>
    <path d="M0 90C80 86 140 136 247 140" stroke="var(--brand-red)" stroke-width="3" fill="none"/>
  </svg>
  <div class="kickplate col-4"></div>

  <svg class="pane pane--tall col-5" viewBox="0 0 247 362" aria-label="Window graphic with friends photo and web address">
    <defs>
      <linearGradient id="glow-5" x1="0" y1="0" x2="0" y2="1">
        <stop offset="0" stop-color="#000"/><stop offset="1" stop-color="#c8121a"/>
      </linearGradient>
      <linearGradient id="photo-5" x1="0" y1="0" x2="1" y2="1">
        <stop offset="0" stop-color="#e9e6e3"/><stop offset="0.5" stop-color="#9a6a52"/><stop offset="1" stop-color="#e06aa0"/>
      </linearGradient>
    </defs>
    <rect width="247" height="362" fill="#000"/>
    <rect y="322" width="247" height="40" fill="url(#glow-5)"/>
    <path role="img" aria-label="Photo of three laughing young women" d="M0 0H247V290C170 285 100 230 0 222Z" fill="url(#photo-5)"/>
    <path d="M0 226C100 234 170 288 247 292" stroke="var(--brand-red)" stroke-width="9" fill="none"/>
    <path d="M0 240C100 248 170 296 247 302" stroke="var(--brand-red)" stroke-width="3" fill="none"/>
    <text class="web-address" x="123.5" y="324" text-anchor="middle" font-size="12.5">mybrookhavendentistry.com</text>
  </svg>
  <div class="kickplate col-5"></div>

  <svg class="pane pane--tall col-6" viewBox="0 0 247 362" aria-label="Window graphic with brand name and woman photo">
    <defs>
      <linearGradient id="glow-6" x1="0" y1="0" x2="0" y2="1">
        <stop offset="0" stop-color="#c8121a"/><stop offset="1" stop-color="#000"/>
      </linearGradient>
      <linearGradient id="photo-6" x1="0" y1="0" x2="0" y2="1">
        <stop offset="0" stop-color="#e9dcc2"/><stop offset="0.6" stop-color="#d9b49a"/><stop offset="1" stop-color="#2f9a4a"/>
      </linearGradient>
    </defs>
    <rect width="247" height="362" fill="#000"/>
    <rect width="247" height="40" fill="url(#glow-6)"/>
    <text class="brand-name" x="123.5" y="62" text-anchor="middle" font-size="29">Brookhaven</text>
    <text class="brand-name" x="220" y="85" text-anchor="end" font-size="12" letter-spacing="4">DENTISTRY</text>
    <path role="img" aria-label="Photo of a smiling blonde woman in a green top" d="M0 175C90 168 150 110 247 106V362H0Z" fill="url(#photo-6)"/>
    <path d="M0 170C90 163 150 104 247 100" stroke="var(--brand-red)" stroke-width="9" fill="none"/>
    <path d="M0 156C90 150 150 96 247 90" stroke="var(--brand-red)" stroke-width="3" fill="none"/>
  </svg>
  <div class="kickplate col-6"></div>

</main>
</body>
</html>
```